Icon-Design für Makeup Artist Webseite
Super creative designs. Exactly what we were looking for!Highly recommended.
Zielgruppe
Sabine Ter Horst Makeup Artist. Zielgruppe 18-34. 'Normale' Personen die lernen wollen wie man Makeup richtig aufträgt.
Aufgabenstellung
Das Projekt besteht darin 5 Icons zu designen. Die Webseite ist noch in der Entwicklung ein Screenshot wie es auf dem Handy aussehen soll finden Sie im Anhang.
Es werden 5 creative Icons benötigt die die Kategorien wiederspiegeln.(Also keine "Langweiligen Icone", diese können ruhig ausgefallen sein, sollten jedoch zum style der Seite passen )
Kategorie 1 = Eye Makeup(Lidschatten) Tutorials. Hier sind Texte + Videos enthalten wie man das Augenmakeup richtig aufträgt + Ausgefallene Looks
Kategorie 2 = Skin Care. Texte+Bilder über Haut+Produkte zur richtigen Pflege seiner Haut.
Kategorie 3 = E-Book. Hier steht ein E-Book-Shop zur verfügung indem man sich E-Book kaufen kann.
Kategorie 4 = About. Hier sind alle Informationen über Sabine enthalten.
Download Button = Dieser sollte auf einem leicht grauen-weißen hintergrund ordentlich zum vorschein kommen.
Der Blaue Farb-Code der Webseite ist : 3b5998

```html
<!DOCTYPE html>
<html lang="en">
<head>
<meta charset="utf-8">
<title>Sabine Ter Horst – Makeup Artist</title>
<link rel="stylesheet" href="https://fonts.googleapis.com/css2?family=Roboto:wght@300;400;500;700&family=Open+Sans:wght@400;600&display=swap">
<style>
  :root{
    --brand-blue:#3b5998;
    --brand-blue-dark:#2f4a82;
    --gold:#c9a23a;
    --gold-dark:#a98424;
    --stage:#94b2c4;
    --white:#ffffff;
    --blush:#f7d3dc;
    --mist:#e6e6e8;
    --ink:#333333;
    --lip-red:#c0303f;
    --lip-pink:#e37f92;
  }
  *{box-sizing:border-box;margin:0;padding:0}
  html,body{width:1200px;height:900px;overflow:hidden}
  body{background:var(--stage);font-family:"Roboto",sans-serif;position:relative}
  .screen{position:absolute;left:350px;top:10px;width:500px;height:880px;background:var(--white);overflow:hidden;box-shadow:0 6px 24px rgba(0,0,0,.18)}
  .app-header{height:105px;background:var(--brand-blue);position:relative;color:var(--white)}
  .status-bar{display:flex;justify-content:space-between;align-items:center;padding:8px 12px 0;font-size:14px;height:30px}
  .status-left,.status-right{display:flex;align-items:center;gap:6px;width:150px}
  .status-right{justify-content:flex-end}
  .battery{width:28px;height:12px;border:1.5px solid var(--white);border-radius:2px;position:relative}
  .battery::after{content:"";position:absolute;left:1px;top:1px;width:5px;height:7px;background:var(--white)}
  .menu-toggle{position:absolute;left:16px;top:55px;width:40px}
  .menu-toggle span{display:block;height:3px;background:var(--white);margin-bottom:8px;border-radius:2px}
  .brand-name{position:absolute;left:0;right:0;top:52px;text-align:center;font-weight:700;font-size:24px;color:var(--gold);letter-spacing:.3px}
  .category-nav{height:95px;display:flex;justify-content:space-around;align-items:flex-start;padding-top:8px;border-bottom:2px solid var(--mist)}
  .category{display:flex;flex-direction:column;align-items:center;width:115px}
  .category-tile{width:68px;height:60px;background:var(--brand-blue);display:flex;align-items:center;justify-content:center;border-radius:3px;box-shadow:inset 0 -6px 0 rgba(0,0,0,.12)}
  .category-tile.is-gold{background:linear-gradient(180deg,var(--gold),var(--gold-dark))}
  .category-label{margin-top:7px;font-size:10px;font-weight:500;color:var(--brand-blue);text-transform:uppercase;white-space:nowrap}
  .category-label.is-gold{color:var(--gold)}
  .promo-colors{height:123px;background:var(--blush);position:relative;text-align:center}
  .promo-colors h2{font-weight:400;font-size:36px;color:var(--ink);padding-top:18px;letter-spacing:.5px}
  .lipstick-strip{position:absolute;left:0;right:0;bottom:0;height:40px;background:linear-gradient(90deg,var(--lip-pink),var(--lip-red) 30%,#7a1f3a 55%,var(--lip-red) 75%,#7b4aa0)}
  .ebook-promo{height:231px;background:var(--mist);position:relative}
  .ebook-copy{position:absolute;left:10px;width:360px;top:54px;text-align:center;color:var(--brand-blue)}
  .ebook-copy .kicker{font-weight:300;font-size:28px;letter-spacing:.5px;line-height:1.1}
  .ebook-copy .title{font-weight:700;font-size:31px;letter-spacing:.5px;line-height:1.05}
  .ebook-copy .subtitle{font-size:11px;color:var(--ink);margin-top:8px}
  .download-button{display:inline-flex;align-items:center;gap:6px;margin-top:20px;background:var(--brand-blue);color:var(--white);font-size:12px;padding:8px 12px;border-radius:5px}
  .ebook-cover{position:absolute;right:22px;top:22px;width:88px;height:168px;background:linear-gradient(160deg,#ffffff,#d9dce4 70%,#3b5998);transform:skewY(-6deg);box-shadow:-4px 6px 10px rgba(0,0,0,.2)}
  .looks-gallery{height:147px;display:flex}
  .look{flex:1;background:linear-gradient(135deg,#d9c5c8,#b68d8e 50%,#4d8fb3)}
  .look + .look{margin-left:3px;background:linear-gradient(135deg,#c9d3dc,#e96fa3 50%,#5cc0d6)}
  .site-footer{height:179px;background:var(--brand-blue);color:var(--white);font-family:"Open Sans",sans-serif}
  .footer-links{display:flex;justify-content:center;gap:148px;padding-top:22px;font-size:19px}
  .social-links{display:flex;justify-content:center;gap:8px;margin-top:34px}
  .social-links span{width:50px;height:50px;border-radius:50%;background:var(--white);color:var(--brand-blue);font-size:8px;font-weight:600;display:flex;align-items:center;justify-content:center}
</style>
</head>
<body>
<main class="screen">
  <header class="app-header">
    <div class="status-bar">
      <div class="status-left"><span>●●●○○</span><span>KALLA</span></div>
      <div class="status-time">4:21 PM</div>
      <div class="status-right"><span>22%</span><span class="battery"></span></div>
    </div>
    <div class="menu-toggle"><span></span><span></span><span></span></div>
    <div class="brand-name">Sabine Ter Horst</div>
  </header>

  <nav class="category-nav">
    <div class="category">
      <div class="category-tile">
        <svg width="44" height="44" viewBox="0 0 44 44" aria-hidden="true">
          <g transform="rotate(-10 22 22)">
            <rect x="7" y="6" width="30" height="32" rx="1.5" fill="#fff"/>
            <rect x="12" y="10" width="20" height="24" fill="#3b5998"/>
            <g fill="#3b5998">
              <rect x="8.5" y="8" width="2" height="3"/><rect x="8.5" y="14" width="2" height="3"/><rect x="8.5" y="20" width="2" height="3"/><rect x="8.5" y="26" width="2" height="3"/><rect x="8.5" y="32" width="2" height="3"/>
              <rect x="33.5" y="8" width="2" height="3"/><rect x="33.5" y="14" width="2" height="3"/><rect x="33.5" y="20" width="2" height="3"/><rect x="33.5" y="26" width="2" height="3"/><rect x="33.5" y="32" width="2" height="3"/>
            </g>
            <path d="M18 16 L27 22 L18 28 Z" fill="#fff"/>
          </g>
        </svg>
      </div>
      <span class="category-label">Tutorials</span>
    </div>
    <div class="category">
      <div class="category-tile">
        <svg width="48" height="44" viewBox="0 0 48 44" aria-hidden="true">
          <path d="M5 18 Q22 4 40 16 Q22 28 5 18 Z" fill="#fff"/>
          <circle cx="22" cy="16.5" r="6" fill="#3b5998"/>
          <circle cx="22" cy="16.5" r="2.6" fill="#fff"/>
          <path d="M8 14 L5 9 M13 10.5 L11 5 M19 9 L18.5 3.5 M25 9 L26 3.5 M31 10.5 L33.5 5.5 M36 13 L40 9" stroke="#fff" stroke-width="1.8" stroke-linecap="round"/>
          <path d="M28 26 L39 37" stroke="#fff" stroke-width="3.5" stroke-linecap="round"/>
          <path d="M24 22 L28.5 26.5 L26 29 L21.5 24.5 Z" fill="#fff"/>
          <path d="M19 20 L24 22 L21.5 24.5 Z" fill="#fff"/>
        </svg>
      </div>
      <span class="category-label">Skin Care</span>
    </div>
    <div class="category">
      <div class="category-tile is-gold">
        <svg width="44" height="44" viewBox="0 0 44 44" aria-hidden="true">
          <rect x="4" y="6" width="36" height="24" rx="2" fill="none" stroke="#fff" stroke-width="2.5"/>
          <path d="M13 11 H27 L31 15 V26 H13 Z" fill="#fff"/>
          <path d="M27 11 V15 H31" fill="none" stroke="#c9a23a" stroke-width="1.2"/>
          <rect x="15.5" y="17" width="13" height="6" rx="1" fill="#c9a23a"/>
          <path d="M17 19 H19 M21 19 V21 M24 19 H27 M24 19 V21" stroke="#fff" stroke-width="1"/>
          <path d="M18 30 L16 37 H28 L26 30" fill="#fff"/>
          <rect x="12" y="37" width="20" height="2.5" rx="1" fill="#fff"/>
        </svg>
      </div>
      <span class="category-label is-gold">Sabine's E-Book</span>
    </div>
    <div class="category">
      <div class="category-tile">
        <svg width="44" height="44" viewBox="0 0 44 44" aria-hidden="true">
          <circle cx="22" cy="23" r="17" fill="#fff"/>
          <circle cx="22" cy="23" r="12.5" fill="#3b5998"/>
          <path d="M22 31 C14 25 15.5 17.5 19.5 17.5 C21 17.5 22 19 22 19 C22 19 23 17.5 24.5 17.5 C28.5 17.5 30 25 22 31 Z" fill="#fff"/>
          <path d="M33 5 L34.2 8.8 L38 10 L34.2 11.2 L33 15 L31.8 11.2 L28 10 L31.8 8.8 Z" fill="#c9a23a"/>
        </svg>
      </div>
      <span class="category-label">About Sabine</span>
    </div>
  </nav>

  <section class="promo-colors">
    <h2>LOVELY COLORS</h2>
    <div class="lipstick-strip" role="img" aria-label="Row of lipsticks in pink, red, berry and purple shades"></div>
  </section>

  <section class="ebook-promo">
    <div class="ebook-copy">
      <p class="kicker">HOW TO APPLY MAKEUP</p>
      <p class="title">LIKE THE PROS DO</p>
      <p class="subtitle">A Simple Guide to Common Makeup Types AND TRICKS</p>
      <span class="download-button"><svg width="14" height="14" viewBox="0 0 14 14" aria-hidden="true"><path d="M7 1 V9 M3 5 L7 9 L11 5 M1 12 H13" stroke="#fff" stroke-width="2" fill="none"/></svg>DOWNLOAD</span>
    </div>
    <div class="ebook-cover" role="img" aria-label="E-book cover with makeup brushes and title"></div>
  </section>

  <section class="looks-gallery">
    <div class="look" role="img" aria-label="Model wearing blue smoky eye makeup"></div>
    <div class="look" role="img" aria-label="Model wearing bright pink and turquoise makeup"></div>
  </section>

  <footer class="site-footer">
    <div class="footer-links"><span>Contact</span><span>About</span></div>
    <div class="social-links">
      <span>Friendly</span><span>Snapline</span><span>Chirper</span><span>Pinwall</span><span>Clipstream</span>
    </div>
  </footer>
</main>
</body>
</html>
```